Franchising Brochure Design Project

We need a serious revamp of our in-house made Franchising Brochure, which currently has 10 pages (possibly due to the way text was laid out).

Brevalink has recently started a rebranding project and we would like to find a suitable designer to help us going through this journey. This is the least technical document and we feel it would be a good start.

We are looking for a bold yet stylish redesign of this document, which should appeal to a global audience, as does our business opportunity.

For the deadline we would like to see a couple pages 3-4 maximum using some of the content we provide.

Target Market(s)

International English-speaking expats who want to set up their own business in international locations around the world.

Industry/Entity Type

Business

Requirements
Must have
• Must be delivered in InDesign or another editable format, as well as High Res PDF

Good imagery - we can help source

```html
<!DOCTYPE html>
<html lang="en">
<head>
<meta charset="utf-8">
<title>Brevalink Franchising – Page 3</title>
<link href="https://fonts.googleapis.com/css2?family=Arimo:wght@400;700&family=EB+Garamond:wght@400;500&display=swap" rel="stylesheet">
<style>
  :root {
    --brand-red: #b5191f;
    --ink: #231f20;
    --muted: #cfcfcf;
    --page-edge: #c8c8c8;
    --chart-bg: #f6f6f6;
    --grid: #e4e4e4;
    --canvas: #ffffff;
  }
  * { margin: 0; padding: 0; box-sizing: border-box; }
  html, body { width: 1200px; height: 1200px; overflow: hidden; background: var(--canvas); }
  .page {
    position: absolute; left: 60px; top: 218px; width: 1080px; height: 764px;
    border: 1px solid var(--page-edge); background: #fff;
  }
  .side-band { position: absolute; right: 0; top: 0; width: 72px; height: 100%; background: var(--brand-red); }
  .page-number {
    position: absolute; right: 0; bottom: 12px; width: 72px; text-align: center;
    font: 700 19px/1 "Arimo", sans-serif; color: #fff;
  }
  .footer-mark {
    position: absolute; left: 29px; bottom: 14px;
    font: 700 13px/1 "Arimo", sans-serif; color: var(--muted);
  }
  .copy {
    position: absolute; left: 50px; top: 106px; width: 470px;
    font: 400 15px/21px "EB Garamond", serif; color: var(--ink);
  }
  .copy h2 {
    font: 400 27px/1.1 "Arimo", sans-serif; color: var(--brand-red); margin-bottom: 1px;
  }
  .copy h3 {
    font: 700 15px/1.2 "Arimo", sans-serif; color: var(--brand-red); margin: 12px 0 3px;
  }
  .copy p { margin-bottom: 8px; }
  .bullets { list-style: none; margin-bottom: 8px; }
  .bullets li { position: relative; padding-left: 18px; }
  .bullets li::before {
    content: ""; position: absolute; left: 0; top: 6px; width: 10px; height: 10px;
    border: 3px solid var(--brand-red); border-radius: 50%;
  }
  .chart-card {
    position: absolute; left: 552px; width: 426px;
    background: var(--chart-bg); border: 1px solid var(--brand-red);
    border-radius: 12px; box-shadow: -5px 5px 0 var(--brand-red);
  }
  .chart-card.users { top: 108px; height: 270px; }
  .chart-card.adspend { top: 416px; height: 280px; }
  .chart-card svg { display: block; width: 100%; height: 100%; }
  .chart-title { font: 700 12px "Arimo", sans-serif; fill: var(--brand-red); }
  .tick { font: 400 6.5px "Arimo", sans-serif; fill: var(--ink); }
  .axis-label { font: 400 6.5px "Arimo", sans-serif; fill: var(--ink); }
  .source { font: 400 6.5px "Arimo", sans-serif; fill: #666; }
  .series { fill: none; stroke: var(--brand-red); stroke-width: 1.3; }
  .marker { fill: #fff; stroke: var(--brand-red); stroke-width: 3; }
  .grid { stroke: var(--grid); stroke-width: 0.6; }
  .baseline { stroke: var(--ink); stroke-width: 1; }
</style>
</head>
<body>
<div class="page">
  <section class="copy">
    <h2>Why an online business?</h2>
    <p>Global Internet usage continues its massive growth, with much of the world spending substantially more time online than watching TV, reading newspapers or listening to the radio.</p>
    <p>And people use it for a myriad of purposes, chiefly:</p>
    <ul class="bullets">
      <li>To find out information</li>
      <li>To buy goods and services</li>
      <li>To sell goods and services</li>
      <li>To connect with other people</li>
    </ul>
    <p>Online advertising spend matches this growth with companies worldwide allocating an ever-increasing share of their annual marketing budget to online campaigns.</p>
    <h3>Why buy a franchise?</h3>
    <p>Why not do it yourself? For many people, the reasons are clear. By buying into an established organisation you benefit in many ways, including:</p>
    <ul class="bullets">
      <li>Access to existing know-how – you don’t need to ‘re-invent the wheel’</li>
      <li>Access to existing IT, design, sales and marketing skills sets – you don’t need to hire in expertise</li>
      <li>Custom back-office systems tailor-made for your business</li>
      <li>The technology is provided (and supported) for you</li>
      <li>The brand equity of an existing, high-growth, international group</li>
      <li>A central sales team brings advertising revenue to you</li>
    </ul>
  </section>

  <figure class="chart-card users">
    <svg viewBox="0 0 355 225" aria-label="Line chart of world Internet users 2000 to 2010 in millions">
      <text class="chart-title" x="14" y="17">World Internet users 2000-2010</text>
      <g>
        <line class="grid" x1="40" x2="342" y1="37" y2="37"/><line class="grid" x1="40" x2="342" y1="52.6" y2="52.6"/>
        <line class="grid" x1="40" x2="342" y1="68.2" y2="68.2"/><line class="grid" x1="40" x2="342" y1="83.8" y2="83.8"/>
        <line class="grid" x1="40" x2="342" y1="99.4" y2="99.4"/><line class="grid" x1="40" x2="342" y1="115" y2="115"/>
        <line class="grid" x1="40" x2="342" y1="130.6" y2="130.6"/><line class="grid" x1="40" x2="342" y1="146.2" y2="146.2"/>
        <line class="grid" x1="40" x2="342" y1="161.8" y2="161.8"/><line class="grid" x1="40" x2="342" y1="177.4" y2="177.4"/>
        <line class="baseline" x1="38" x2="342" y1="193" y2="193"/>
      </g>
      <g class="tick" text-anchor="end">
        <text x="36" y="39">2000</text><text x="36" y="54.6">1800</text><text x="36" y="70.2">1600</text>
        <text x="36" y="85.8">1400</text><text x="36" y="101.4">1200</text><text x="36" y="117">1000</text>
        <text x="36" y="132.6">800</text><text x="36" y="148.2">600</text><text x="36" y="163.8">400</text>
        <text x="36" y="179.4">200</text><text x="36" y="195">0</text>
      </g>
      <text class="axis-label" transform="translate(18 113) rotate(-90)" text-anchor="middle">Millions</text>
      <g class="tick" text-anchor="middle">
        <text x="55" y="203">2000</text><text x="82.3" y="203">2001</text><text x="109.6" y="203">2002</text>
        <text x="136.9" y="203">2003</text><text x="164.2" y="203">2004</text><text x="191.5" y="203">2005</text>
        <text x="218.8" y="203">2006</text><text x="246.1" y="203">2007</text><text x="273.4" y="203">2008</text>
        <text x="300.7" y="203">2009</text><text x="328" y="203">2010</text>
      </g>
      <polyline class="series" points="55,169.6 82.3,159.5 109.6,148.5 136.9,142.3 164.2,131.4 191.5,121.2 218.8,111.9 246.1,101 273.4,79.9 300.7,59.6 328,40.1"/>
      <g class="marker">
        <circle cx="55" cy="169.6" r="4.5"/><circle cx="82.3" cy="159.5" r="4.5"/><circle cx="109.6" cy="148.5" r="4.5"/>
        <circle cx="136.9" cy="142.3" r="4.5"/><circle cx="164.2" cy="131.4" r="4.5"/><circle cx="191.5" cy="121.2" r="4.5"/>
        <circle cx="218.8" cy="111.9" r="4.5"/><circle cx="246.1" cy="101" r="4.5"/><circle cx="273.4" cy="79.9" r="4.5"/>
        <circle cx="300.7" cy="59.6" r="4.5"/><circle cx="328" cy="40.1" r="4.5"/>
      </g>
      <text class="source" x="341" y="215" text-anchor="end">Source: Global Net Metrics</text>
    </svg>
  </figure>

  <figure class="chart-card adspend">
    <svg viewBox="0 0 355 233" aria-label="Line chart of world Internet advertising revenues 2000 to 2010 in USD billions">
      <text class="chart-title" x="14" y="17">World Internet advertising revenues 2000-2010</text>
      <g>
        <line class="grid" x1="40" x2="342" y1="35" y2="35"/><line class="grid" x1="40" x2="342" y1="60.8" y2="60.8"/>
        <line class="grid" x1="40" x2="342" y1="86.7" y2="86.7"/><line class="grid" x1="40" x2="342" y1="112.5" y2="112.5"/>
        <line class="grid" x1="40" x2="342" y1="138.3" y2="138.3"/><line class="grid" x1="40" x2="342" y1="164.2" y2="164.2"/>
        <line class="baseline" x1="38" x2="342" y1="190" y2="190"/>
      </g>
      <g class="tick" text-anchor="end">
        <text x="36" y="37">30</text><text x="36" y="62.8">25</text><text x="36" y="88.7">20</text>
        <text x="36" y="114.5">15</text><text x="36" y="140.3">10</text><text x="36" y="166.2">5</text><text x="36" y="192">0</text>
      </g>
      <text class="axis-label" transform="translate(18 112) rotate(-90)" text-anchor="middle">USD Billions</text>
      <g class="tick" text-anchor="middle">
        <text x="55" y="200">2000</text><text x="82.3" y="200">2001</text><text x="109.6" y="200">2002</text>
        <text x="136.9" y="200">2003</text><text x="164.2" y="200">2004</text><text x="191.5" y="200">2005</text>
        <text x="218.8" y="200">2006</text><text x="246.1" y="200">2007</text><text x="273.4" y="200">2008</text>
        <text x="300.7" y="200">2009</text><text x="328" y="200">2010</text>
      </g>
      <polyline class="series" points="55,149.7 82.3,156.9 109.6,161.1 136.9,146.6 164.2,131.1 191.5,116.1 218.8,101.1 246.1,86.7 273.4,70.6 300.7,73.7 328,47.4"/>
      <g class="marker">
        <circle cx="55" cy="149.7" r="4.5"/><circle cx="82.3" cy="156.9" r="4.5"/><circle cx="109.6" cy="161.1" r="4.5"/>
        <circle cx="136.9" cy="146.6" r="4.5"/><circle cx="164.2" cy="131.1" r="4.5"/><circle cx="191.5" cy="116.1" r="4.5"/>
        <circle cx="218.8" cy="101.1" r="4.5"/><circle cx="246.1" cy="86.7" r="4.5"/><circle cx="273.4" cy="70.6" r="4.5"/>
        <circle cx="300.7" cy="73.7" r="4.5"/><circle cx="328" cy="47.4" r="4.5"/>
      </g>
      <text class="source" x="341" y="220" text-anchor="end">Source: Harbridge Analytics LLP</text>
    </svg>
  </figure>

  <div class="footer-mark">Brevalink Franchising</div>
  <div class="side-band"></div>
  <div class="page-number">3</div>
</div>
</body>
</html>
```